I am a company selling interior designing materials

HI, I am selling interior design materials and require a namecard which is more outstanding while following a certain details placement as attached.

My clients are mainly interior designers so it has to attract their attention rather than feeling that its "just another namecard". I am selling wallcoverings, fabrics, acoustics and carpets.

Target Market(s)

interior designers designing hotels, commerical offices.

Contact Information for Business Card

As per attached.
Please change address to 47 Jalan 16 Tampines #05-02 Velmora Building Singapore 527314

Font styles to use
Other font styles liked:
• calibri

Requirements
Must have
• (1) company logo on top in the middle. Placement of contac details to be the same
• (2) company color is blue/green cymk 75/8/42/0
• (3) "KTV" logo to be prominent
• (4) You may change the logo but there should be a "swirl" surrounding the word KTV like current logo. The swirl pattern does not need to follow current logo and you may propose.
Should not have
• (1) there should not be any designs above "KTV" logo
• (2) no sharp triangles or angles

```html
<!DOCTYPE html>
<html lang="en">
<head>
<meta charset="utf-8">
<title>KTV Business Card</title>
<link href="https://fonts.googleapis.com/css2?family=Carlito:wght@400;700&family=Roboto+Slab:wght@700&display=swap" rel="stylesheet">
<style>
  :root {
    --backdrop: #2e2e2e;
    --teal: #1fa598;
    --card-white: #f3f3f3;
    --ink-grey: #5a5a5a;
    --brand-red: #ee1e24;
    --white: #ffffff;
  }
  * { margin: 0; padding: 0; box-sizing: border-box; }
  html, body {
    width: 1200px; height: 960px; overflow: hidden;
    background: var(--backdrop);
    font-family: "Carlito", "Calibri", sans-serif;
  }
  .card {
    position: absolute;
    width: 598px; height: 342px;
    border-radius: 18px;
    overflow: hidden;
  }
  .card-front { left: 322px; top: 108px; background: var(--teal); }
  .card-back { left: 320px; top: 493px; width: 600px; background: var(--brand-red); }

  .front-curve { position: absolute; inset: 0; }

  .brand-block {
    position: absolute; left: 30px; top: 128px; width: 270px;
    text-align: center; color: var(--ink-grey);
  }
  .brand-name {
    font-weight: 700; font-size: 40px; letter-spacing: 1px; line-height: 1;
  }
  .company-name {
    margin-top: 22px; font-weight: 700; font-size: 13.5px; white-space: nowrap;
  }

  .contact {
    position: absolute; right: 22px; top: 86px;
    text-align: right; color: var(--white);
    font-size: 15.5px; line-height: 19.5px;
  }
  .contact-name {
    font-family: "Roboto Slab", serif;
    font-size: 19px; letter-spacing: 0.5px; margin-bottom: 18px;
  }
  .contact-address { margin-bottom: 9px; }

  .back-brand {
    position: absolute; left: 0; right: 0; top: 135px;
    text-align: center; color: var(--white);
    font-weight: 700; font-size: 68px; line-height: 1; letter-spacing: 2px;
  }
  .services {
    position: absolute; left: 0; right: 0; bottom: 26px;
    text-align: center; color: var(--white);
    font-weight: 700; font-size: 15.5px;
  }
</style>
</head>
<body>
  <section class="card card-front">
    <svg class="front-curve" width="598" height="342" viewBox="0 0 598 342" aria-hidden="true">
      <ellipse cx="40" cy="178" rx="324" ry="200" fill="none" stroke="var(--white)" stroke-width="2"/>
      <ellipse cx="30" cy="176" rx="318" ry="196" fill="var(--card-white)"/>
    </svg>
    <div class="brand-block">
      <div class="brand-name">KTV</div>
      <div class="company-name">KaTaVia Interior Furnishings Pte Ltd</div>
    </div>
    <div class="contact">
      <div class="contact-name">JOANNE LIM</div>
      <div class="contact-address">47 Jalan 16 Tampines<br>#05-02 ,Velmora<br>Building Singapore 527314</div>
      <div>M. (65) 9172 4630</div>
      <div>joanne@ktvfurnishing.com</div>
      <div>www.ktvfurnishing.com</div>
    </div>
  </section>

  <section class="card card-back">
    <div class="back-brand">KTV</div>
    <div class="services">Wallcoverings &nbsp;• Acoustic &nbsp;• Fabrics &nbsp;• Carpet</div>
  </section>
</body>
</html>
```